Easy one-page Web Design with ready made sketch/template

This project have an already made one page Web Design sketch/template that should be used as a base. It needs professional touch and improvements but should be quite straight forward for you to make.

Webpage: Offers local graphical design services

Attached following documents for you:
- PSD sketch
- JPG sketch
- Word file with project description (read carefully)
- Logo

Reason: Project extended to get the final designs submitted. Thanks

Target Market(s)

Logo design

Industry/Entity Type

Graphic Design

Number of Pages Required

1 page

Requirements
Must have
• Please refer to attached word document.
Nice to have
Should not have

```html
<!DOCTYPE html>
<html lang="sv">
<head>
<meta charset="utf-8">
<title>Ritkontoret – Logodesign</title>
<link rel="stylesheet" href="https://fonts.googleapis.com/css2?family=Roboto:wght@400;500;700&family=Oswald:wght@400;500&display=swap">
<style>
  :root {
    --wood-dark: #2b231e;
    --wood-mid: #4a3d34;
    --wood-light: #5e5047;
    --brand-blue: #1ea4dd;
    --pill-grey: #7a7a7a;
    --pill-dark: #3d3d3f;
    --pill-border: #bdbdbd;
    --text-light: #ffffff;
    --badge-yellow: #f4b21d;
    --badge-orange: #f7891c;
    --badge-green: #27a24a;
    --badge-edge: #2a2a2a;
    --gold: #b8892a;
  }
  * { box-sizing: border-box; margin: 0; padding: 0; }
  html, body { width: 1200px; height: 1000px; overflow: hidden; }
  body { font-family: "Roboto", Arial, sans-serif; color: var(--text-light); background: var(--wood-dark); }

  .page { position: relative; width: 1200px; height: 1000px; overflow: hidden; }

  .hero-photo {
    position: absolute; inset: 0;
    background:
      radial-gradient(ellipse at 70% 20%, rgba(190,180,170,.35), transparent 40%),
      radial-gradient(ellipse at 60% 30%, rgba(0,0,0,.25), transparent 30%),
      linear-gradient(100deg, var(--wood-dark) 0%, var(--wood-mid) 45%, var(--wood-light) 70%, var(--wood-mid) 100%);
  }

  /* Header */
  .site-header { position: absolute; top: 0; left: 0; right: 0; height: 130px; }
  .brand { position: absolute; left: 22px; top: 26px; display: flex; align-items: center; gap: 12px; }
  .brand-square { width: 34px; height: 34px; background: var(--brand-blue); }
  .brand-name { font-size: 40px; font-weight: 500; color: var(--brand-blue); letter-spacing: 1px; }

  .main-nav { position: absolute; left: 336px; top: 60px; display: flex; gap: 22px; }
  .nav-pill {
    width: 120px; height: 34px; border-radius: 17px;
    background: var(--pill-grey); border: 2px solid #5a5a5a;
    font-size: 15px; font-weight: 500; text-align: center; line-height: 30px;
  }

  .search-bar {
    position: absolute; left: 900px; top: 12px; width: 250px; height: 24px;
    border-radius: 12px; background: rgba(60,60,60,.85); border: 1px solid #777;
  }
  .search-button { position: absolute; left: 1154px; top: 10px; width: 28px; height: 28px; }

  .order-button {
    position: absolute; left: 1036px; top: 50px; width: 148px; height: 44px;
    border-radius: 6px; background: var(--pill-grey); border: 2px solid #d6d6d6;
    font-size: 18px; font-weight: 700; text-align: center; line-height: 40px;
  }

  /* Hero call to action */
  .hero-cta { position: absolute; left: 0; right: 0; top: 400px; display: flex; flex-direction: column; align-items: center; gap: 14px; }
  .cta-pill {
    height: 40px; border-radius: 20px; background: var(--pill-dark);
    border: 3px solid var(--pill-border); display: flex; align-items: center; justify-content: center;
    font-size: 17px; padding: 0 22px;
  }
  .cta-how { width: 236px; gap: 10px; font-size: 18px; }
  .cta-how .q { font-size: 28px; font-weight: 500; }
  .cta-from { width: 170px; height: 36px; }
  .cta-price { width: 110px; height: 36px; }

  /* Feature badges */
  .badge {
    position: absolute; border: 3px solid var(--badge-edge);
    box-shadow: 0 4px 10px rgba(0,0,0,.5); font-family: "Oswald", "Roboto", sans-serif;
    text-transform: uppercase; text-align: center;
  }
  .badge-guarantee { left: 244px; top: 800px; width: 246px; height: 156px; background: var(--badge-yellow); }
  .guarantee-seal { position: absolute; left: 46px; top: 8px; width: 138px; height: 132px; border-radius: 8px; background: var(--gold); }

  .badge-order { left: 472px; top: 752px; width: 270px; height: 150px; background: var(--badge-orange); z-index: 2; }
  .badge-order .title { margin-top: 12px; font-size: 17px; letter-spacing: 1px; }
  .badge-order .clock { display: block; margin: 8px auto 4px; }
  .badge-order .price { font-size: 16px; letter-spacing: 1px; }
  .order-tail { position: absolute; left: 118px; bottom: -24px; }

  .badge-rating { left: 716px; top: 800px; width: 254px; height: 160px; background: var(--badge-green); overflow: hidden; }
  .rating-stripe { position: absolute; left: 0; top: 0; }
  .rating-score { position: absolute; left: 18px; top: 22px; font-size: 20px; color: var(--badge-edge); }
  .rating-stars { position: absolute; left: 64px; top: 22px; padding: 0 8px; background: #2b2b2b; color: var(--badge-yellow); font-size: 18px; letter-spacing: 2px; }
  .rating-text { position: absolute; left: 82px; top: 72px; font-size: 15px; letter-spacing: 1px; }
  .rating-count { position: absolute; left: 100px; top: 116px; font-size: 14px; letter-spacing: 1px; }
</style>
</head>
<body>
<main class="page">
  <div class="hero-photo" role="img" aria-label="Fotografi uppifrån av ett mörkt träskrivbord med kaffekopp, bärbar dator, glasögon, mobiltelefon, anteckningsblock och pennor"></div>

  <header class="site-header">
    <div class="brand">
      <span class="brand-square"></span>
      <span class="brand-name">Ritkontoret</span>
    </div>

    <nav class="main-nav">
      <span class="nav-pill">Products</span>
      <span class="nav-pill">Gallery</span>
      <span class="nav-pill">FAQ</span>
      <span class="nav-pill">Contact Us</span>
    </nav>

    <div class="search-bar"></div>
    <svg class="search-button" viewBox="0 0 28 28" aria-label="Sök">
      <circle cx="14" cy="14" r="13" fill="#4a4a4a" stroke="#888"/>
      <circle cx="12.5" cy="12.5" r="5" fill="none" stroke="#fff" stroke-width="2"/>
      <line x1="16" y1="16" x2="20" y2="20" stroke="#fff" stroke-width="2.4" stroke-linecap="round"/>
    </svg>

    <div class="order-button">ORDER LOGO</div>
  </header>

  <section class="hero-cta">
    <div class="cta-pill cta-how">
      <svg width="18" height="18" viewBox="0 0 18 18"><polygon points="2,2 16,9 2,16" fill="var(--brand-blue)"/></svg>
      <span>HOW IT WORKS</span><span class="q">?</span>
    </div>
    <div class="cta-pill cta-from">Start From</div>
    <div class="cta-pill cta-price">$ 1495</div>
  </section>

  <section class="feature-badges">
    <div class="badge badge-guarantee">
      <div class="guarantee-seal"></div>
    </div>

    <div class="badge badge-order">
      <p class="title">Beställ logotyp</p>
      <svg class="clock" width="56" height="56" viewBox="0 0 56 56">
        <circle cx="28" cy="28" r="26" fill="#3a2c26" stroke="#fff" stroke-width="3"/>
        <circle cx="28" cy="28" r="17" fill="#fff"/>
        <text x="28" y="33" text-anchor="middle" font-family="Oswald, sans-serif" font-size="15" fill="#3a2c26">24</text>
      </svg>
      <p class="price">Från 1495:-</p>
      <svg class="order-tail" width="34" height="24" viewBox="0 0 34 24">
        <polygon points="0,0 34,0 17,22" fill="var(--badge-orange)" stroke="var(--badge-edge)" stroke-width="3"/>
        <rect x="2" y="0" width="30" height="3" fill="var(--badge-orange)"/>
      </svg>
    </div>

    <div class="badge badge-rating">
      <svg class="rating-stripe" width="80" height="160" viewBox="0 0 80 160">
        <polygon points="0,0 80,0 30,160 0,160" fill="var(--badge-yellow)"/>
      </svg>
      <span class="rating-score">9.0</span>
      <span class="rating-stars">★★★★★</span>
      <span class="rating-text">Snittbetyg från kunder</span>
      <span class="rating-count">120 omdömen</span>
    </div>
  </section>
</main>
</body>
</html>
```